Road Construction Company needs business cards

We would like a new business card designed for our business.

We're a road construction company based in Qld, Australia.

Can the business card please have the following information on it.

Name: Brent Malvoy
Position: General Manager
Phone: 0471 592 304
Email: Brent.malvoy@quendix.com.au
Address: 87 Harrowgate Ave, Pindarra, QLD, 4000
Website: www.quendix.com.au

Visually we'd like the card to be professional and simple.

Attached is our logo.

Our website is www.quendix.com.au

Target Market(s)

Men aged 25-60

Contact Information for Business Card

As listed in project description

Font styles to use
Serif

Requirements
Must have
• Large logo on back of card

```html
<!DOCTYPE html>
<html lang="en">
<head>
<meta charset="utf-8">
<title>Quendix Road Construction — Business Card</title>
<link href="https://fonts.googleapis.com/css2?family=Michroma&display=swap" rel="stylesheet">
<style>
  :root {
    --backdrop: #636363;
    --card: #ffffff;
    --ink: #1b57a5;
    --rule: #1b57a5;
  }
  * { margin: 0; padding: 0; box-sizing: border-box; }
  html, body {
    width: 1072px;
    height: 1200px;
    overflow: hidden;
    background: var(--backdrop);
    font-family: "Michroma", sans-serif;
    color: var(--ink);
  }
  .sheet {
    position: relative;
    width: 1072px;
    height: 1200px;
  }
  .card {
    position: absolute;
    top: 471px;
    width: 449px;
    height: 257px;
    background: var(--card);
  }
  .card--front { left: 69px; }
  .card--back { left: 554px; }

  .wordmark {
    position: absolute;
    inset: 0;
    display: flex;
    align-items: center;
    justify-content: center;
    font-size: 30px;
    letter-spacing: 1px;
    color: var(--ink);
  }

  .contact {
    position: absolute;
    left: 43px;
    top: 78px;
    font-size: 7px;
    letter-spacing: 0.6px;
    line-height: 1;
  }
  .contact__name { font-size: 8px; }
  .contact__name strong {
    font-weight: 400;
    font-size: 11px;
    letter-spacing: 0.8px;
  }
  .contact__position {
    margin-top: 6px;
    padding-left: 12px;
    font-size: 6.4px;
  }
  .contact__rule {
    width: 153px;
    height: 1px;
    background: var(--rule);
    margin-top: 14px;
    margin-bottom: 14px;
  }
  .contact__line { margin-bottom: 6px; font-size: 6.6px; }
</style>
</head>
<body>
  <main class="sheet">
    <section class="card card--front" aria-label="Card front">
      <div class="wordmark">QUENDIX</div>
    </section>

    <section class="card card--back" aria-label="Card back">
      <div class="contact">
        <p class="contact__name">Name: Brent <strong>Malvoy</strong></p>
        <p class="contact__position">Position: General Manager</p>
        <div class="contact__rule"></div>
        <p class="contact__line">Email: Brent.malvoy@quendix.com.au</p>
        <p class="contact__line">Address: 87 Harrowgate Ave, Pindarra, QLD, 4000</p>
        <p class="contact__line">Phone: 0471 592 304</p>
        <p class="contact__line">Website: www.quendix.com.au</p>
      </div>
    </section>
  </main>
</body>
</html>
```